Tamrock Stationery Design Project

company name : Tamrock General Trading LLC.
light watermark taken from the logo to cover almost the middle of the stationary..
logo is attached and an on going business card project is released on the same company name..
thanks
Reason: more time for more designs and to work with comfort..
Industry/Entity Type
Business
Colors
Designer to choose colors to be used in the design.
Look and feel
Each slider illustrates characteristics of the customer's brand and the style your logo design should communicate.

```html
<!DOCTYPE html>
<html lang="en">
<head>
<meta charset="utf-8">
<title>Tamrock Int. Stationery</title>
<link href="https://fonts.googleapis.com/css2?family=Cinzel:wght@500&family=Montserrat:wght@400;500;600&display=swap" rel="stylesheet">
<style>
  :root{
    --backdrop:#929396;
    --paper:#ffffff;
    --ink:#3a3b3e;
    --ink-soft:#4a4b4f;
    --brand-blue:#1a67b1;
    --name-blue:#1565b5;
    --band-start:#19b4e3;
    --band-end:#173f8a;
    --tab-dark:#3b3c3f;
    --watermark:#ececec;
    --edge:#b9babc;
  }
  *{box-sizing:border-box;margin:0;padding:0}
  html,body{width:1200px;height:640px;overflow:hidden}
  body{background:var(--backdrop);position:relative;font-family:"Montserrat",Arial,sans-serif;color:var(--ink)}
  .sheet{position:absolute;background:var(--paper);box-shadow:1px 2px 3px rgba(0,0,0,.25);overflow:hidden}
  .wordmark{font-family:"Cinzel",Georgia,serif;font-weight:500;color:var(--ink);white-space:nowrap;letter-spacing:.02em}
  .footer-bar{position:absolute;left:0;bottom:0;width:100%;display:block}
  .icon{display:inline-block;width:1.25em;height:1.25em;border-radius:50%;background:var(--brand-blue);vertical-align:middle;margin-right:.35em;position:relative}
  .icon svg{position:absolute;inset:0;width:100%;height:100%}
  .contact-line{white-space:nowrap;line-height:1.4}

  /* letterhead */
  .letterhead{left:24px;top:43px;width:430px;height:557px}
  .letterhead .wordmark{position:absolute;left:32px;top:62px;font-size:18px}
  .letterhead .address{position:absolute;right:90px;top:50px;font-size:5.5px;text-align:right;line-height:1.35}
  .letterhead .divider{position:absolute;left:346px;top:38px;width:1px;height:38px;background:#c9cacc}
  .letterhead .contacts{position:absolute;left:350px;top:38px;font-size:5.5px}
  .letterhead .watermark{position:absolute;left:92px;top:290px;font-size:38px;color:var(--watermark)}

  /* business card */
  .card-front{left:595px;top:44px;width:267px;height:152px}
  .card-front .holder{position:absolute;right:17px;top:22px;text-align:right}
  .card-front .holder-name{font-size:11.5px;font-weight:600;color:var(--name-blue)}
  .card-front .holder-role{font-size:6.5px;color:var(--ink)}
  .card-front .contacts{position:absolute;left:17px;top:75px;font-size:7.5px}
  .card-front .address{position:absolute;left:17px;top:112px;font-size:7px;line-height:1.35}
  .card-front .wordmark{position:absolute;right:20px;top:113px;font-size:12.5px}

  /* logo cards */
  .card-logo{left:894px;top:40px;width:266px;height:152px;display:flex;align-items:center;justify-content:center}
  .card-logo .wordmark{font-size:28px}
  .card-reverse{left:894px;top:234px;width:266px;height:152px;background:var(--brand-blue);display:flex;align-items:center;justify-content:center}
  .card-reverse .wordmark{font-size:28px;color:var(--paper)}

  /* envelope front */
  .envelope-front{left:479px;top:234px;width:383px;height:173px}
  .envelope-front .wordmark{position:absolute;left:31px;top:48px;font-size:12.5px}
  .envelope-front .contacts{position:absolute;top:70px;font-size:4.8px}
  .envelope-front .contacts.phones{left:31px}
  .envelope-front .contacts.web{left:73px;padding-left:4px;border-left:1px solid #c9cacc}
  .envelope-front .address{position:absolute;left:31px;top:88px;font-size:5px;line-height:1.35}
  .envelope-front .watermark{position:absolute;left:228px;top:96px;font-size:24px;color:var(--watermark)}

  /* envelope back */
  .envelope-back{left:482px;top:432px;width:380px;height:171px;border:1px solid var(--edge)}
  .envelope-back .flap{position:absolute;left:0;top:0;width:100%;height:48px}
  .envelope-back .wordmark{position:absolute;left:0;right:0;top:14px;text-align:center;font-size:11px}
</style>
</head>
<body>

<svg width="0" height="0" style="position:absolute" aria-hidden="true">
  <defs>
    <linearGradient id="band-gradient" x1="0" x2="1" y1="0" y2="0">
      <stop offset="0" stop-color="#19b4e3"/>
      <stop offset="1" stop-color="#173f8a"/>
    </linearGradient>
    <symbol id="glyph-phone" viewBox="0 0 10 10"><path d="M3 2.3h1.3l.5 1.5-.8.6a4 4 0 0 0 1.6 1.6l.6-.8 1.5.5V7a.8.8 0 0 1-.8.8A5 5 0 0 1 2.2 3a.8.8 0 0 1 .8-.7z" fill="#fff"/></symbol>
    <symbol id="glyph-mobile" viewBox="0 0 10 10"><rect x="3.5" y="2.2" width="3" height="5.6" rx=".5" fill="#fff"/></symbol>
    <symbol id="glyph-mail" viewBox="0 0 10 10"><rect x="2.4" y="3.2" width="5.2" height="3.6" fill="#fff"/><path d="M2.4 3.2 5 5.2l2.6-2" stroke="#1a67b1" stroke-width=".5" fill="none"/></symbol>
    <symbol id="glyph-web" viewBox="0 0 10 10"><circle cx="5" cy="5" r="2.7" fill="none" stroke="#fff" stroke-width=".7"/><path d="M2.3 5h5.4M5 2.3v5.4" stroke="#fff" stroke-width=".5"/></symbol>
  </defs>
</svg>

<!-- Letterhead -->
<section class="sheet letterhead">
  <div class="wordmark">Tamrock Int.</div>
  <div class="address">48 Harbor Lane East<br>Port City, PO Box 20417, USA</div>
  <div class="divider"></div>
  <div class="contacts">
    <div class="contact-line"><span class="icon"><svg><use href="#glyph-phone"/></svg></span>(00) 007 2300</div>
    <div class="contact-line"><span class="icon"><svg><use href="#glyph-mobile"/></svg></span>(00) 007 2300</div>
    <div class="contact-line"><span class="icon"><svg><use href="#glyph-mail"/></svg></span>info@tamrockmail.com</div>
    <div class="contact-line"><span class="icon"><svg><use href="#glyph-web"/></svg></span>www.tamrockint.com</div>
  </div>
  <div class="wordmark watermark">Tamrock Int.</div>
  <svg class="footer-bar" viewBox="0 0 430 18" height="18" preserveAspectRatio="none" aria-hidden="true">
    <polygon points="0,9 258,9 254,18 0,18" fill="url(#band-gradient)"/>
    <path d="M260 18 L266 3 Q267.5 0 271 0 L430 0 L430 18 Z" fill="var(--tab-dark)"/>
  </svg>
</section>

<!-- Business card front -->
<section class="sheet card-front">
  <div class="holder">
    <div class="holder-name">Daniel Harper</div>
    <div class="holder-role">Director</div>
  </div>
  <div class="contacts">
    <div class="contact-line"><span class="icon"><svg><use href="#glyph-phone"/></svg></span>(00) 007 2300</div>
    <div class="contact-line"><span class="icon"><svg><use href="#glyph-mobile"/></svg></span>(00) 007 2300</div>
    <div class="contact-line"><span class="icon"><svg><use href="#glyph-mail"/></svg></span>info@tamrockmail.com</div>
  </div>
  <div class="address">48 Harbor Lane East<br>Port City, PO Box 20417, USA</div>
  <div class="wordmark">Tamrock Int.</div>
  <svg class="footer-bar" viewBox="0 0 267 13" height="13" preserveAspectRatio="none" aria-hidden="true">
    <polygon points="0,6.5 157,6.5 154,13 0,13" fill="url(#band-gradient)"/>
    <path d="M159 13 L163 2.5 Q164 0 167 0 L267 0 L267 13 Z" fill="var(--tab-dark)"/>
  </svg>
</section>

<!-- Logo card -->
<section class="sheet card-logo">
  <div class="wordmark">Tamrock Int.</div>
</section>

<!-- Reverse logo card -->
<section class="sheet card-reverse">
  <div class="wordmark">Tamrock Int.</div>
</section>

<!-- Envelope front -->
<section class="sheet envelope-front">
  <div class="wordmark">Tamrock Int.</div>
  <div class="contacts phones">
    <div class="contact-line"><span class="icon"><svg><use href="#glyph-phone"/></svg></span>(00) 007 2300</div>
    <div class="contact-line"><span class="icon"><svg><use href="#glyph-mobile"/></svg></span>(00) 007 2300</div>
  </div>
  <div class="contacts web">
    <div class="contact-line"><span class="icon"><svg><use href="#glyph-mail"/></svg></span>info@tamrockmail.com</div>
    <div class="contact-line"><span class="icon"><svg><use href="#glyph-web"/></svg></span>www.tamrockint.com</div>
  </div>
  <div class="address">48 Harbor Lane East<br>Port City, PO Box 20417, USA</div>
  <div class="wordmark watermark">Tamrock Int.</div>
  <svg class="footer-bar" viewBox="0 0 383 17" height="17" preserveAspectRatio="none" aria-hidden="true">
    <polygon points="0,10 225,10 222,17 0,17" fill="url(#band-gradient)"/>
    <path d="M227 17 L232 3 Q233 0 237 0 L383 0 L383 17 Z" fill="var(--tab-dark)"/>
  </svg>
</section>

<!-- Envelope back -->
<section class="sheet envelope-back">
  <svg class="flap" viewBox="0 0 380 48" preserveAspectRatio="none" aria-hidden="true">
    <path d="M0 0 L20 40 Q24 47 32 47 L348 47 Q356 47 360 40 L380 0" fill="none" stroke="#6e6f72" stroke-width=".8"/>
  </svg>
  <div class="wordmark">Tamrock Int.</div>
</section>

</body>
</html>
```